Domestic Cleaning services needs a website

We need a descriptive, easy to use and trust inspiring website for domestic cleaning clients. It should be easy to use, with appointment scheduling and SMS notifiers. The brand name "BrightNest by Marisol" should be associated with all offers at the website. blue/green/white colors should be more pronounced.
Website should be Mobile friendly.

Target Market(s)

Domestic Market. Long rental tourists, expats, local housewifes

Logo Text

BRIGHTNEST by MARISOL

Number of Pages Required

2 page

Font styles to use
Sans Serif

```html
<!DOCTYPE html>
<html lang="en">
<head>
<meta charset="utf-8">
<title>BrightNest by Marisol — Domestic Cleaning</title>
<link rel="stylesheet" href="https://fonts.googleapis.com/css2?family=Montserrat:wght@400;600;700&family=Open+Sans:wght@400;600&display=swap">
<style>
:root{
  --green:#1f9a3c;
  --blue:#1565c8;
  --ink:#222;
  --text:#444;
  --muted:#777;
  --grey-band:#efefef;
  --white:#fff;
  --red:#d9322b;
  --footer-bar:#d6d6d6;
}
*{box-sizing:border-box;margin:0;padding:0}
html,body{width:1200px;height:3030px;overflow:hidden;background:var(--white)}
body{position:relative;font-family:"Open Sans",Arial,sans-serif;color:var(--text)}
.abs{position:absolute}
.heading{font-family:"Montserrat",Arial,sans-serif;font-weight:700;color:var(--ink);font-size:19px;text-align:center;width:100%;left:0}
.heading-light{color:var(--white)}
.rule{position:absolute;left:572px;width:56px;height:5px;background:var(--green)}
.btn{position:absolute;display:flex;align-items:center;justify-content:center;color:var(--white);font-family:"Montserrat",Arial,sans-serif;font-size:10px;background:var(--green)}
.photo{position:absolute;border-radius:50%;box-shadow:inset 0 0 0 1px rgba(0,0,0,.06)}

/* header */
.site-header{position:absolute;top:0;left:0;width:1200px;height:103px;background:var(--white)}
.brand{position:absolute;display:flex;align-items:center;gap:10px;font-family:"Montserrat",Arial,sans-serif;font-weight:600;color:var(--blue)}
.brand-mark{width:20px;height:22px;background:var(--green)}
.brand-name{font-size:27px;line-height:1}
.brand-by{font-size:11px;line-height:1.3}
.main-nav a{position:absolute;top:34px;height:27px;display:flex;align-items:center;justify-content:center;color:var(--white);text-decoration:none;font-size:14px;background:var(--blue)}
.main-nav a.is-active{background:var(--green)}
.call-line{position:absolute;left:495px;top:69px;font-size:10px;font-weight:600;color:var(--ink)}
.call-line span{color:var(--green)}

/* hero */
.hero{position:absolute;top:103px;left:0;width:1200px;height:379px;
  background:linear-gradient(115deg,#cfcfcc 0%,#f4f4f2 22%,#e6e6e3 38%,#f7f4ee 50%,#e7dccb 58%,#d9cdb9 64%,#2f6fb0 69%,#e9e9e6 74%,#c4c4c0 88%,#a9a9a5 100%)}
.hero-dots{position:absolute;left:921px;top:454px;width:79px;height:28px;background:var(--green);display:flex;align-items:center;justify-content:center;gap:7px}
.hero-dots i{width:9px;height:9px;border-radius:50%;background:var(--white)}
.hero-dots i:first-child{background:#2b2b2b}

/* overview */
.overview{position:absolute;top:482px;left:0;width:1200px;height:199px;background:var(--grey-band)}
.lede{position:absolute;left:0;width:100%;text-align:center;font-size:13.5px;color:var(--text)}

/* services */
.service-title{position:absolute;width:180px;text-align:center;font-family:"Montserrat",Arial,sans-serif;font-weight:600;font-size:12px;color:#333}
.service-sub{position:absolute;width:180px;text-align:center;font-size:11px;color:var(--muted)}

/* promotions */
.promotions{position:absolute;top:1119px;left:0;width:1200px;height:385px;
  background:linear-gradient(160deg,#9c9893 0%,#d9d6d2 25%,#efeeec 45%,#b8b4b0 60%,#5d5a58 75%,#3c3a39 88%,#8e8b89 100%)}
.promo-card{position:absolute;top:1282px;height:167px;background:#f1f1f1;text-align:center;padding-top:28px}
.promo-card h3{font-family:"Montserrat",Arial,sans-serif;font-weight:700;font-size:12px;color:var(--ink)}
.promo-card hr{border:0;height:1px;background:#bbb;width:140px;margin:10px auto 8px}
.promo-card p{font-size:11px;line-height:1.35;color:#555;padding:0 30px}

/* team */
.member-name{position:absolute;width:160px;text-align:center;font-family:"Montserrat",Arial,sans-serif;font-weight:600;font-size:12px;color:#333}

/* testimonials */
.testimonials{position:absolute;top:1976px;left:0;width:1200px;height:356px;
  background:linear-gradient(180deg,#232c38 0%,#35404d 35%,#56606a 58%,#a0826a 72%,#c48f5e 76%,#4c4032 82%,#2a2520 100%)}
.quote-text{position:absolute;left:201px;top:2211px;width:615px;font-size:12px;line-height:1.5;color:var(--white)}
.t-dots{position:absolute;left:912px;top:2291px;display:flex;gap:6px}
.t-dots i{width:4px;height:4px;border-radius:50%;background:#aaa}

/* orders */
.orders-visual{position:absolute;left:201px;top:2486px;width:800px;height:201px;
  background:linear-gradient(100deg,#2f3134 0%,#55585c 18%,#9a9da1 35%,#c9cbce 48%,#e2c3ad 58%,#3f7fc9 66%,#b8babd 74%,#6a6d71 88%,#3a3c3f 100%)}
.step{position:absolute;width:30px;height:30px;border-radius:50%;background:var(--blue);color:var(--white);font-size:11px;display:flex;align-items:center;justify-content:center;font-weight:600}
.social-btn{position:absolute;display:flex;align-items:center;justify-content:center;color:var(--white);font-family:"Montserrat",Arial,sans-serif;font-size:12px}

/* footer */
.site-footer{position:absolute;top:2743px;left:0;width:1200px;height:266px;background:var(--white);border-top:1px solid #e2e2e2}
.col-title{position:absolute;font-family:"Montserrat",Arial,sans-serif;font-size:11px;font-weight:400;color:#333;letter-spacing:.5px}
.col-list{position:absolute;list-style:none;font-size:11px;line-height:19px;color:#333}
.col-divider{position:absolute;top:2790px;width:1px;height:130px;background:#ccc}
.contact dt{font-weight:600;font-size:11px;color:#222;margin-top:8px}
.contact dd{font-size:11px;color:#666;line-height:16px}
.pay-box{position:absolute;left:643px;top:2933px;width:143px;height:50px;border:1px solid #bbb;display:flex;flex-wrap:wrap;align-content:center;gap:4px;padding:6px}
.pay-box i{width:28px;height:14px;background:#c9ced6}
.pay-box i.wide{width:56px;background:#8aa0c2}
.bottom-bar{position:absolute;top:3009px;left:0;width:1200px;height:21px;background:var(--footer-bar);font-size:8px;color:#555;padding:6px 0 0 201px}
</style>
</head>
<body>

<header class="site-header">
  <div class="brand" style="left:201px;top:26px">
    <span class="brand-mark"></span>
    <span><span class="brand-name" style="display:block">BrightNest</span><span class="brand-by">by Marisol</span></span>
  </div>
  <nav class="main-nav">
    <a class="is-active" href="#" style="left:493px;width:86px">Home Page</a>
    <a href="#" style="left:588px;width:87px">About Us</a>
    <a href="#" style="left:684px;width:87px">Services</a>
    <a href="#" style="left:779px;width:89px">Login</a>
  </nav>
  <p class="call-line">Cal Us Now : <span>01000 555 120</span></p>
  <svg class="abs" style="left:970px;top:32px" width="26" height="24" viewBox="0 0 26 24" aria-label="Messages">
    <path d="M3 6h14v9H9l-4 4v-4H3z" fill="#c9c9c9"/>
    <circle cx="19" cy="6" r="5" fill="var(--red)"/>
  </svg>
</header>

<section class="hero" role="img" aria-label="Photo of a scrubbing brush cleaning a soapy tiled floor"></section>
<div class="hero-dots"><i></i><i></i><i></i></div>

<section class="overview">
  <h2 class="heading abs" style="top:44px">Overview</h2>
  <span class="rule" style="top:84px"></span>
  <p class="lede" style="top:119px">Lorem ipsum dolor sit amet, consectetuer adipiscing elit. Aenean commodo ligula eget dolor.</p>
</section>

<section class="services">
  <h2 class="heading abs" style="top:714px">How May We Be Of Service?</h2>
  <span class="rule" style="top:758px"></span>

  <div class="photo" role="img" aria-label="Photo of window cleaning" style="left:231px;top:813px;width:96px;height:96px;background:linear-gradient(120deg,#f4f6f7 0%,#9fd0e4 35%,#2f7fa8 60%,#1e4f6c 100%)"></div>
  <div class="photo" role="img" aria-label="Photo of ironing clothes" style="left:389px;top:813px;width:96px;height:96px;background:linear-gradient(160deg,#e9e4e0 0%,#c9b3a8 35%,#4fb3b7 60%,#2f5b78 100%)"></div>
  <div class="photo" role="img" aria-label="Photo of a squeegee on glass" style="left:554px;top:813px;width:96px;height:96px;background:linear-gradient(135deg,#78b8ee 0%,#2a74c6 45%,#1a3f73 70%,#5c6f82 100%)"></div>
  <div class="photo" role="img" aria-label="Photo of exterior cleaning" style="left:713px;top:813px;width:96px;height:96px;background:linear-gradient(135deg,#f3f0ea 0%,#e7a46a 35%,#c0672d 65%,#7c3d1a 100%)"></div>
  <div class="photo" role="img" aria-label="Photo of dry cleaned shirts" style="left:873px;top:813px;width:96px;height:96px;background:linear-gradient(120deg,#f2f4f7 0%,#b8cde4 35%,#7d9cc2 65%,#4c6a90 100%)"></div>

  <h3 class="service-title" style="left:189px;top:934px">FAMILY PACKAGE</h3>
  <h3 class="service-title" style="left:347px;top:934px">EXTRA CLEAN</h3>
  <h3 class="service-title" style="left:512px;top:934px">EXPAT SOLO</h3>
  <h3 class="service-title" style="left:671px;top:934px">EXPAT PRO</h3>
  <h3 class="service-title" style="left:831px;top:934px">CREATE YOUR OWN</h3>

  <p class="service-sub" style="left:189px;top:967px">Interior Cleaning</p>
  <p class="service-sub" style="left:347px;top:967px">Ironing</p>
  <p class="service-sub" style="left:512px;top:967px">Windows</p>
  <p class="service-sub" style="left:671px;top:967px">Exterior Cleaning</p>
  <p class="service-sub" style="left:831px;top:967px">Dry Cleaning</p>

  <a class="btn" style="left:234px;top:1016px;width:90px;height:36px">Read More</a>
  <a class="btn" style="left:392px;top:1016px;width:90px;height:36px">Read More</a>
  <a class="btn" style="left:557px;top:1016px;width:90px;height:36px">Read More</a>
  <a class="btn" style="left:716px;top:1016px;width:90px;height:36px">Read More</a>
  <a class="btn" style="left:876px;top:1016px;width:90px;height:36px">Read More</a>
</section>

<section class="promotions" role="img" aria-label="Photo of a hand signing a document with a pen"></section>
<h2 class="heading heading-light abs" style="top:1163px;font-size:17px">OUR PROMOTIONS</h2>
<span class="rule" style="top:1203px"></span>
<article class="promo-card" style="left:201px;width:262px"><h3>SUMMER MADNESS</h3><hr><p>Lorem ipsum dolor sit amet, consectetuer adipiscing elit. Aenean commodo ligula eget dolor.</p></article>
<article class="promo-card" style="left:471px;width:258px"><h3>AFTER PARTY</h3><hr><p>Lorem ipsum dolor sit amet, consectetuer adipiscing elit. Aenean commodo ligula eget dolor.</p></article>
<article class="promo-card" style="left:739px;width:262px"><h3>SUPERFAST</h3><hr><p>Lorem ipsum dolor sit amet, consectetuer adipiscing elit. Aenean commodo ligula eget dolor.</p></article>

<section class="team">
  <h2 class="heading abs" style="top:1546px">About Your Team</h2>
  <span class="rule" style="top:1587px"></span>

  <div class="photo" role="img" aria-label="Portrait of team member Rosa T" style="left:200px;top:1648px;width:171px;height:171px;background:radial-gradient(circle at 50% 45%,#e7c4ae 0%,#c99a80 22%,#3a2620 42%,#5a4a44 60%,#e2e2e2 80%)"></div>
  <div class="photo" role="img" aria-label="Portrait of team member Tomas Reyes" style="left:356px;top:1648px;width:171px;height:171px;background:radial-gradient(circle at 50% 50%,#e3bfa3 0%,#c69876 22%,#2f2420 42%,#151515 62%,#dcdcdc 82%)"></div>
  <div class="photo" role="img" aria-label="Portrait of team member Dan K Moreno" style="left:515px;top:1648px;width:171px;height:171px;background:radial-gradient(circle at 50% 45%,#e0b394 0%,#c58d68 25%,#4a3326 42%,#1e1e1e 64%,#d8d8d8 82%)"></div>
  <div class="photo" role="img" aria-label="Portrait of team member Ilse Varga" style="left:678px;top:1648px;width:171px;height:171px;background:radial-gradient(circle at 50% 45%,#f1d6c2 0%,#e2b89a 22%,#d9b98a 40%,#f4f4f4 62%,#e4e4e4 82%)"></div>
  <div class="photo" role="img" aria-label="Portrait of team member Priya Lund" style="left:832px;top:1648px;width:171px;height:171px;background:radial-gradient(circle at 50% 45%,#efcdb6 0%,#d8a98b 22%,#5a3a2a 42%,#f0f0f0 64%,#e6e6e6 82%)"></div>

  <h3 class="member-name" style="left:205px;top:1845px">ROSA T</h3>
  <h3 class="member-name" style="left:361px;top:1845px">TOMAS REYES</h3>
  <h3 class="member-name" style="left:520px;top:1845px">DAN K MORENO</h3>
  <h3 class="member-name" style="left:683px;top:1845px">ILSE VARGA</h3>
  <h3 class="member-name" style="left:837px;top:1845px">PRIYA LUND</h3>

  <a class="btn" style="left:237px;top:1879px;width:90px;height:39px">Read More</a>
  <a class="btn" style="left:396px;top:1879px;width:90px;height:39px">Read More</a>
  <a class="btn" style="left:555px;top:1879px;width:90px;height:39px">Read More</a>
  <a class="btn" style="left:718px;top:1879px;width:90px;height:39px">Read More</a>
  <a class="btn" style="left:872px;top:1879px;width:90px;height:39px">Read More</a>
</section>

<section class="testimonials" role="img" aria-label="Photo of wind turbines on a plain at dusk"></section>
<h2 class="heading heading-light abs" style="top:2026px">Testimonials</h2>
<span class="rule" style="top:2066px;background:var(--white)"></span>
<p class="abs" style="left:201px;top:2128px;font-family:Montserrat,Arial,sans-serif;font-size:12px;font-weight:600;color:var(--white)">What Our Clients Are Saying</p>
<span class="abs" style="left:201px;top:2166px;width:34px;height:3px;background:var(--white)"></span>
<svg class="abs" style="left:760px;top:2140px" width="32" height="26" viewBox="0 0 32 26" aria-label="Quotation mark">
  <path d="M2 24V14C2 7 6 3 12 2v4c-3 1-5 3-5 7h5v11zM18 24V14c0-7 4-11 10-12v4c-3 1-5 3-5 7h5v11z" fill="#ddd"/>
</svg>
<p class="quote-text">Lorem ipsum dolor sit amet, consectetuer adipiscing elit. Aenean commodo ligula eget dolor. Aenean massa. Cum sociis natoque penatibus et magnis dis parturient montes, nascetur ridiculus mus.</p>
<p class="abs" style="left:201px;top:2276px;font-size:11px;color:#ddd">Donec pede justo - USA</p>
<div class="photo" role="img" aria-label="Portrait of a smiling client" style="left:867px;top:2104px;width:137px;height:137px;border:4px solid var(--white);background:radial-gradient(circle at 50% 45%,#f0d2bc 0%,#dcae8e 24%,#e0c27e 44%,#f2f2f2 66%,#e8e8e8 84%)"></div>
<div class="t-dots"><i></i><i></i><i></i><i></i><i></i><i></i><i></i></div>

<section class="orders">
  <h2 class="heading abs" style="top:2390px">Awaiting Your Orders</h2>
  <span class="rule" style="top:2431px"></span>
  <div class="orders-visual" role="img" aria-label="Photo of a hand wiping a stove top with a blue cloth"></div>
  <p class="abs" style="left:257px;top:2522px;font-family:Montserrat,Arial,sans-serif;font-size:12px;font-weight:600;color:var(--white)">Simple Registration</p>
  <span class="step" style="left:257px;top:2559px">1</span>
  <span class="step" style="left:508px;top:2559px">2</span>
  <span class="step" style="left:782px;top:2559px">3</span>
  <a class="social-btn" style="left:253px;top:2600px;width:182px;height:34px;background:var(--blue)">Login with Linkly</a>
  <a class="social-btn" style="left:508px;top:2600px;width:201px;height:34px;background:var(--green)">Sign in with Searchly</a>
  <a class="social-btn" style="left:786px;top:2594px;width:106px;height:48px;background:var(--red);font-weight:700;font-size:11px;text-align:center;line-height:1.1">REGISTER<br>NOW</a>
</section>

<footer class="site-footer">
  <div class="brand" style="left:201px;top:48px">
    <span class="brand-mark" style="width:16px;height:18px"></span>
    <span><span class="brand-name" style="display:block;font-size:22px;color:#444">BrightNest</span><span class="brand-by" style="font-size:9px;color:#444">by Marisol</span></span>
  </div>
</footer>
<span class="col-divider" style="left:647px"></span>
<span class="col-divider" style="left:793px"></span>
<h4 class="col-title" style="left:534px;top:2788px">NAVIGATION</h4>
<ul class="col-list" style="left:534px;top:2815px"><li>Home Page</li><li>About Us</li><li>Services</li><li>Login</li></ul>
<h4 class="col-title" style="left:686px;top:2788px">FOLLOW US</h4>
<ul class="col-list" style="left:686px;top:2815px"><li>Linkly</li><li>Chirper</li><li>Searchly Plus</li><li>RSS</li></ul>
<h4 class="col-title" style="left:814px;top:2788px">CONTACT US</h4>
<dl class="contact abs" style="left:814px;top:2808px">
  <dt>Telephone:</dt><dd>Number: 01632 960 418</dd>
  <dt>Email Address:</dt><dd>hello@brightnest-home.com</dd>
  <dt>Offices:</dt><dd>Registered Office 4,<br>Meadow Lane, Oxbury OX9 2LT</dd>
</dl>
<p class="abs" style="left:529px;top:2954px;font-size:9px;color:#555;letter-spacing:.5px">PAYMENT OPTIONS</p>
<div class="pay-box" role="img" aria-label="Accepted payment methods">
  <i class="wide"></i><i></i><i></i><i></i><i></i>
</div>
<div class="bottom-bar">© 2017 BrightNest Services Limited. All rights reserved.</div>

</body>
</html>
```